Label Design for Climbing Chalk (fitness category)

I am looking for someone to design a front and back label for a bottle of liquid chalk. Liquid chalk is used in gyms, gymnastics, climbing to prevent your hands from getting moist and increase friction. I'm uploading some design motivations that I like.

The bottle is going to be black and I want the label to be clear. You have free reign of how you want to approach this design. Below are more specifics for the sizing:

*Attached is a picture of a competitor product (Tor Hold Liquid Chalk). Please don't use this for motivation, their label is very bad. I'm attaching a picture so that you can see what the bottle looks like.
*Attached are design motivations that I like
*The bottle is 50 ml, it's 3.75 inches tall, 2 inches wide and 1.25 inches in depth.
*The label can be square or oval (it's up to you). The size of the label needs to be 1,25 x 2.25 inches.
*Name of the product: Varnel Liquid Chalk
*Label needs to have the following Required Text. You can arrange it however you like:
- (50 ml)
- Made by USA Competitive Athletes for Athletes. Increases grip and lasts 3-4 times longer than regular chalk.
- Directions: Shake well. Squeeze some Varnel Liquid Chalk into your hand and rub your hands together. Let your hands air dry for about 10 seconds. To remove the chalk wash your hands with light soap.
Warning: Avoid contact with Eyes. Do not use on broken skin. Do not ingest. Keep out of reach of small children.
- Ingredients: Magnesium carbonate, SD Alcohol, hydroxypropylcellulose, colophonium.

Target Market(s)

Fitness, Athletes, Rock Climbers, Weight Lifters, Gymnasts, etc

Industry/Entity Type

Fitness

Font styles to use
Sans Serif

Colors

Designer to choose colors to be used in the design.

Requirements
Must have
• Please see Project Description for required text. The bottle is going to be black and I want the clear label so please be creative with the colors that would look good
Nice to have
• Please see attached branding ideas that I liked for font and colors. You don't have to strictly stick to them, these are just some of the ones I liked. Be creative and put your best foot forward.

```html
<!DOCTYPE html>
<html lang="en">
<head>
<meta charset="utf-8">
<title>Varnel Liquid Chalk – Front and Back Labels</title>
<link rel="stylesheet" href="https://fonts.googleapis.com/css2?family=Roboto+Condensed:wght@900&family=Mulish:ital,wght@0,400;0,500;1,400;1,500;1,700;1,800&display=swap">
<style>
  :root {
    --label-red: #c1272d;
    --label-white: #ffffff;
    --ink: #111111;
    --band-grey: #c9c9c9;
    --page-bg: #ffffff;
    --shadow: rgba(0, 0, 0, 0.38);
  }
  * { margin: 0; padding: 0; box-sizing: border-box; }
  html, body {
    width: 1200px;
    height: 1029px;
    overflow: hidden;
    background: var(--page-bg);
  }
  .canvas {
    position: relative;
    width: 1200px;
    height: 1029px;
    font-family: "Mulish", sans-serif;
    color: var(--ink);
  }

  /* Label shell: white edge, red ring, white face */
  .label-edge {
    position: absolute;
    width: 442px;
    height: 786px;
    background: var(--label-white);
    border-radius: 50% / 32%;
    filter: drop-shadow(14px 22px 18px var(--shadow));
  }
  .label-edge--front { left: 128px; top: 128px; }
  .label-edge--back  { left: 648px; top: 124px; }

  .label-ring {
    position: absolute;
    left: 10px;
    top: 10px;
    width: 422px;
    height: 766px;
    background: var(--label-red);
    border-radius: 50% / 31%;
  }
  .label-face {
    position: absolute;
    left: 28px;
    top: 28px;
    width: 366px;
    height: 710px;
    background: var(--label-white);
    border-radius: 50% / 28%;
    overflow: hidden;
  }

  .climb-art {
    position: absolute;
    background: var(--label-red);
  }
  .climb-art--front {
    left: 118px; top: 0; width: 260px; height: 126px;
    border-bottom-left-radius: 70px 90px;
  }
  .climb-art--back {
    left: 148px; top: 8px; width: 100px; height: 54px;
    border-top-right-radius: 60px 54px;
    border-bottom-left-radius: 30px 40px;
  }

  .brand-name {
    position: absolute;
    left: 0;
    width: 100%;
    text-align: center;
    font-family: "Roboto Condensed", sans-serif;
    font-weight: 900;
    color: var(--label-red);
    line-height: 1;
  }
  .brand-name--front { top: 132px; font-size: 104px; }
  .brand-name--back  { top: 48px;  font-size: 60px; }

  .product-type {
    position: absolute;
    left: 0;
    width: 100%;
    text-align: center;
    font-family: "Roboto Condensed", sans-serif;
    font-weight: 900;
    text-transform: uppercase;
  }
  .product-type--front { top: 252px; font-size: 92px; line-height: 84px; }
  .product-type--back  { top: 116px; font-size: 42px; line-height: 32px; }

  .ridge-band {
    position: absolute;
    left: 0;
    top: 424px;
    width: 100%;
    height: 184px;
    background: linear-gradient(to bottom, rgba(201,201,201,0) 0, var(--band-grey) 30px, var(--band-grey) 100%);
  }
  .claim {
    position: absolute;
    left: 0;
    top: 472px;
    width: 100%;
    text-align: center;
    font-style: italic;
    font-weight: 500;
    font-size: 21px;
    line-height: 24px;
    letter-spacing: 0.4px;
  }
  .claim .wide { letter-spacing: 2px; }
  .volume {
    position: absolute;
    left: 0;
    top: 646px;
    width: 100%;
    text-align: center;
    font-style: italic;
    font-weight: 500;
    font-size: 30px;
    letter-spacing: 1px;
  }

  .info {
    position: absolute;
    left: 16px;
    width: 334px;
  }
  .info-heading {
    color: var(--label-red);
    font-style: italic;
    font-weight: 800;
    font-size: 21px;
    line-height: 26px;
    letter-spacing: 0.5px;
  }
  .info-body span {
    display: block;
    font-size: 17.5px;
    line-height: 24px;
    letter-spacing: 0.9px;
    text-align: justify;
    text-align-last: justify;
    white-space: nowrap;
  }
  .info-body span.last { text-align-last: left; }
  .info--directions { top: 202px; }
  .info--warning    { top: 388px; }

  .divider {
    position: absolute;
    left: 46px;
    top: 516px;
    width: 272px;
    height: 9px;
    background: var(--label-red);
  }
  .ingredients {
    position: absolute;
    left: 0;
    top: 548px;
    width: 100%;
    text-align: center;
    font-style: italic;
  }
  .ingredients-heading {
    font-weight: 800;
    font-size: 20px;
    line-height: 26px;
  }
  .ingredients-list {
    font-size: 18px;
    line-height: 24px;
    letter-spacing: 0.4px;
  }
</style>
</head>
<body>
<main class="canvas">

  <section class="label-edge label-edge--front" aria-label="Front label">
    <div class="label-ring">
      <div class="label-face">
        <div class="climb-art climb-art--front" role="img" aria-label="Silhouette of a climber hanging from a red rock overhang"></div>
        <h1 class="brand-name brand-name--front">Varnel</h1>
        <p class="product-type product-type--front">Liquid<br>Chalk</p>
        <div class="ridge-band" role="img" aria-label="Grey mountain ridge silhouette"></div>
        <p class="claim">
          Made by USA Competitive<br>
          <span class="wide">Athletes for Athletes.</span><br>
          Increases grip and lasts<br>
          4-3 times longer than<br>
          regular chalk.
        </p>
        <p class="volume">50 ml</p>
      </div>
    </div>
  </section>

  <section class="label-edge label-edge--back" aria-label="Back label">
    <div class="label-ring">
      <div class="label-face">
        <div class="climb-art climb-art--back" role="img" aria-label="Small silhouette of a climber on a red rock overhang"></div>
        <h2 class="brand-name brand-name--back">Varnel</h2>
        <p class="product-type product-type--back">Liquid<br>Chalk</p>

        <div class="info info--directions">
          <h3 class="info-heading">Directions:</h3>
          <p class="info-body">
            <span>Shake well. Squeeze some Varnel</span>
            <span>Liquid Chalk into your hand and rub</span>
            <span>your hands together. Let your hands</span>
            <span>air dry for about 10 seconds. To</span>
            <span>remove the chalk wash your hands</span>
            <span class="last">with light soap.</span>
          </p>
        </div>

        <div class="info info--warning">
          <h3 class="info-heading">Warning:</h3>
          <p class="info-body">
            <span>Avoid contact with Eyes. Do not use</span>
            <span>on broken skin. Do not ingest. Keep</span>
            <span class="last">out of reach of small children.</span>
          </p>
        </div>

        <div class="divider"></div>

        <div class="ingredients">
          <h3 class="ingredients-heading">Ingredients:</h3>
          <p class="ingredients-list">
            Magnesium carbonate, SD Alcohol,<br>
            hydroxypropylcellulose,<br>
            colophonium.
          </p>
        </div>
      </div>
    </div>
  </section>

</main>
</body>
</html>
```